Business Card Design Project

We need a business card design for a management consultancy focused on financial innovation and digital money, run by experts from the Financial Services, Telecoms and Money Transfer industries.
Our products include services such as Mobile Payments, Mobile Money, Digital Wallets, Online Payments, Branchless Banking and more. We work with regulatory information, business plans, financial modelling, strategic planning, new products functional specification, new technologies evaluation, etc.
See company logo attached.
We would like to see 2 versions: one in portuguese and one in english (regarding data information). You can see below information needed (whenever there is a difference between the two versions, the first one is in english and the second one in portuguese).

Name
Position
Phone/ Tel: ++55-11-xxxx-xxxx
Cell/ Cel: ++55-11-9 xxxx-xxxx
Dr. Tavares Lobato Av., 318 - Tower II - 16th floor / Avenida Dr. Tavares Lobato, 318 - Torre II - 16o. andar
São Paulo - SP
01327-118 - Brazil/ 01327-118 - Brasil

Target Market(s)

Audience: C-level executives from banks, credit card companies, acquirers, IT developers, retailers

Industry/Entity Type

Financial

Requirements
Must have
• Must use the logo and information above. Front must have white background. Back side should have only logo.
Nice to have
• Back should be in another colour but if it seems too exxagerated, maintain back in white also.
Should not have
• Do not add other illustrations to the business card.

```html
<!DOCTYPE html>
<html lang="en">
<head>
<meta charset="utf-8">
<title>Veltra Management Consulting – Business Cards</title>
<link href="https://fonts.googleapis.com/css2?family=Cabin:wght@400;500;600&family=Cormorant+Garamond:wght@600&display=swap" rel="stylesheet">
<style>
  :root {
    --stage: #1b1e20;
    --card-blue: #1c22a8;
    --card-white: #f7f7f7;
    --ink-dark: #2a2a2a;
    --ink-grey: #4a4a4a;
    --ink-blue: #2a2fb0;
    --mark-white: #ffffff;
  }
  * { margin: 0; padding: 0; box-sizing: border-box; }
  html, body {
    width: 1200px;
    height: 696px;
    overflow: hidden;
    background: var(--stage);
  }
  .stage {
    position: relative;
    width: 1200px;
    height: 696px;
    display: flex;
    align-items: center;
    justify-content: center;
    gap: 60px;
  }
  .card {
    width: 520px;
    height: 300px;
    position: relative;
    box-shadow: 0 10px 30px rgba(0,0,0,0.45);
  }
  /* Back side */
  .card--back {
    background: var(--card-blue);
    display: flex;
    align-items: center;
    justify-content: center;
  }
  .brand {
    display: flex;
    align-items: center;
    gap: 12px;
    font-family: "Cabin", sans-serif;
    font-weight: 500;
  }
  .brand__square {
    width: 34px;
    height: 34px;
  }
  .brand__name {
    letter-spacing: 0.04em;
    line-height: 1.05;
    text-transform: uppercase;
  }
  .brand__name span { display: block; }
  .brand__name .brand__main { font-size: 30px; }
  .brand__name .brand__sub { font-size: 13.5px; letter-spacing: 0.08em; }
  .card--back .brand { color: var(--mark-white); }
  .card--back .brand__square { background: var(--mark-white); }

  /* Front side */
  .card--front {
    background: var(--card-white);
    padding: 26px 28px;
    font-family: "Cabin", sans-serif;
  }
  .card--front .brand { color: var(--ink-dark); gap: 8px; }
  .card--front .brand__square { width: 20px; height: 20px; background: var(--ink-blue); }
  .card--front .brand__main { font-size: 17px; }
  .card--front .brand__sub { font-size: 7.5px; }
  .person {
    position: absolute;
    top: 24px;
    right: 28px;
    text-align: right;
  }
  .person__name {
    font-family: "Cormorant Garamond", serif;
    font-weight: 600;
    font-size: 18px;
    letter-spacing: 0.03em;
    color: var(--ink-dark);
    text-transform: uppercase;
  }
  .person__role {
    font-size: 10px;
    color: var(--ink-grey);
    margin-top: 2px;
  }
  .person__role .pt { color: var(--ink-blue); }
  .contact {
    position: absolute;
    top: 120px;
    list-style: none;
    font-size: 11.5px;
    line-height: 1.95;
  }
  .contact--en { left: 40px; color: var(--ink-grey); }
  .contact--pt { right: 40px; color: var(--ink-blue); }
</style>
</head>
<body>
  <main class="stage">
    <section class="card card--back" aria-label="Card back">
      <div class="brand">
        <span class="brand__square"></span>
        <div class="brand__name">
          <span class="brand__main">Veltra</span>
          <span class="brand__sub">Management Consulting</span>
        </div>
      </div>
    </section>

    <section class="card card--front" aria-label="Card front">
      <div class="brand">
        <span class="brand__square"></span>
        <div class="brand__name">
          <span class="brand__main">Veltra</span>
          <span class="brand__sub">Management Consulting</span>
        </div>
      </div>

      <div class="person">
        <p class="person__name">Rafael Moreira</p>
        <p class="person__role">Marketing Manager / <span class="pt">Gerente de Marketing</span></p>
      </div>

      <ul class="contact contact--en">
        <li>Phone : ++55-11-xxxx-xxxx</li>
        <li>Cell &nbsp;&nbsp;&nbsp;: ++55-11-9 xxxx-xxxx</li>
        <li>Dr. Tavares Lobato Av., 318</li>
        <li>Tower II - 16th floor</li>
        <li>São Paulo - SP</li>
        <li>01327-118 - Brazil</li>
      </ul>

      <ul class="contact contact--pt">
        <li>Telefone : ++55-11-xxxx-xxxx</li>
        <li>Célula &nbsp;&nbsp;: ++55-11-9 xxxx-xxxx</li>
        <li>Avenida Dr. Tavares Lobato, 318</li>
        <li>Torre II - 16o. andar</li>
        <li>São Paulo - SP</li>
        <li>01327-118 - Brasil</li>
      </ul>
    </section>
  </main>
</body>
</html>
```